Somebody commencing retirement at age 67 and wanting a card to introduce myself

Something that depicts the activities I intend to pursue in retirement: Travel, Golf (both in Australia and internationally), wining (red) and dining and generally leading a decadent lifestyle with my wife (or by myself as appropriate).

I offer no services, but intend to have a decadent, relaxing
retirement, playing golf, drinking red wine and dining at good
restaurants!

The card needs to have a suitably designed logo that reflects the
foregoing.

Requirements
Must have
• On the front of the card, my photograph (attached and cropped as
• appropriate), my name (Carl Brimstead), my mobile phone number (+61 417
• 532 148), my email address (carl@brimstead.example.au) and my residential
• address (41 Kestrel Lane, Marlowe Heights, Western Australia 6031,
• Australia).
• The rear of the card should have my postal address (Carl Brimstead
• Post Office Box 518 Dunmore Western Australia 6947, Australia.)._

```html
<!DOCTYPE html>
<html lang="en">
<head>
<meta charset="utf-8">
<title>Carl Brimstead – Business Card</title>
<link rel="stylesheet" href="https://fonts.googleapis.com/css2?family=Montserrat:wght@800&family=Open+Sans:wght@400;600&display=swap">
<style>
  :root {
    --bg: #3c3d40;
    --orange: #e4542a;
    --orange-light: #eb6a23;
    --orange-deep: #d44a22;
    --stripe: #c9401c;
    --stripe-dark: #b93a18;
    --stripe-light: #d24820;
    --black: #0d0d0d;
    --white: #ffffff;
    --ink: #1b1b1b;
    --photo-warm: #d9d3a8;
    --photo-green: #9aae78;
  }
  * { box-sizing: border-box; margin: 0; padding: 0; }
  html, body { width: 1200px; height: 900px; overflow: hidden; }
  body {
    background: radial-gradient(circle at 60% 40%, #4a4b4f, var(--bg) 70%);
    font-family: "Open Sans", Arial, sans-serif;
    position: relative;
  }
  .card {
    position: absolute;
    left: 337px;
    width: 525px;
    height: 300px;
    border-radius: 22px;
    overflow: hidden;
    box-shadow: 0 10px 24px rgba(0,0,0,.45);
  }

  /* Rear side */
  .card--back {
    top: 110px;
    background: linear-gradient(135deg, var(--orange-light), var(--orange-deep));
  }
  .brand {
    position: absolute;
    top: 82px;
    left: 0;
    width: 100%;
    display: flex;
    justify-content: center;
    align-items: center;
    gap: 12px;
  }
  .brand__dot {
    width: 22px; height: 22px;
    border-radius: 50%;
    background: var(--ink);
  }
  .brand__name {
    font-weight: 600;
    font-size: 30px;
    color: var(--ink);
  }
  .postal {
    position: absolute;
    left: 120px;
    bottom: 58px;
    display: flex;
    align-items: center;
    gap: 10px;
    color: var(--ink);
    font-size: 14px;
    line-height: 1.15;
  }
  .postal__icon {
    flex: none;
    width: 28px; height: 28px;
    border-radius: 50%;
    background: var(--ink);
    display: flex; align-items: center; justify-content: center;
  }

  /* Front side */
  .card--front {
    top: 490px;
    background: var(--orange);
  }
  .photo-backdrop {
    position: absolute;
    left: 0; top: 0;
    width: 230px; height: 300px;
    background: linear-gradient(180deg, var(--photo-warm), var(--photo-green));
  }
  .stripes { position: absolute; left: 0; top: 0; }
  .portrait {
    position: absolute;
    left: 72px; top: 62px;
    width: 176px; height: 176px;
    border-radius: 50%;
    border: 4px solid #222;
    background: radial-gradient(circle at 50% 40%, #c9a57e, #5e7f48 70%);
  }
  .name-band {
    position: absolute;
    left: 246px; top: 68px;
    width: 279px; height: 40px;
    background: var(--black);
    display: flex; align-items: center;
    padding-left: 22px;
  }
  .name-band__text {
    font-family: "Montserrat", Arial, sans-serif;
    font-weight: 800;
    font-size: 21px;
    letter-spacing: .5px;
    color: var(--white);
    text-transform: uppercase;
    white-space: nowrap;
  }
  .contacts {
    position: absolute;
    left: 290px; top: 126px;
    width: 222px;
    list-style: none;
    color: var(--white);
    font-size: 12px;
    line-height: 1.15;
  }
  .contacts__item {
    display: flex;
    align-items: center;
    gap: 10px;
    margin-bottom: 14px;
    white-space: nowrap;
  }
  .contacts__icon { flex: none; width: 18px; height: 18px; }
</style>
</head>
<body>

  <section class="card card--back" aria-label="Card rear">
    <div class="brand">
      <span class="brand__dot"></span>
      <span class="brand__name">Carl Brimstead</span>
    </div>
    <div class="postal">
      <span class="postal__icon">
        <svg width="16" height="16" viewBox="0 0 16 16"><path d="M8 2 1.5 8h2v6h3.5v-4h2v4h3.5V8h2z" fill="#e4542a"/></svg>
      </span>
      <span>Post Office Box 518, Dunmore<br>Western Australia 6947, Australia</span>
    </div>
  </section>

  <section class="card card--front" aria-label="Card front">
    <div class="photo-backdrop" role="img" aria-label="Outdoor landscape backdrop behind portrait"></div>
    <svg class="stripes" width="525" height="300" viewBox="0 0 525 300">
      <polygon points="220,0 250,0 268,300 238,300" fill="var(--stripe-dark)"/>
      <polygon points="250,0 275,0 290,300 268,300" fill="var(--stripe)"/>
      <polygon points="275,0 300,0 312,300 290,300" fill="var(--stripe-light)"/>
    </svg>
    <div class="portrait" role="img" aria-label="Portrait photograph of Carl Brimstead"></div>
    <div class="name-band"><span class="name-band__text">Carl Brimstead</span></div>
    <ul class="contacts">
      <li class="contacts__item">
        <svg class="contacts__icon" viewBox="0 0 18 18"><path d="M9 1a5 5 0 0 0-5 5c0 4 5 10 5 10s5-6 5-10a5 5 0 0 0-5-5zm0 7a2 2 0 1 1 0-4 2 2 0 0 1 0 4z" fill="#111"/></svg>
        <span>41 Kestrel Lane, Marlowe Heights<br>Western Australia 6031, Australia</span>
      </li>
      <li class="contacts__item">
        <svg class="contacts__icon" viewBox="0 0 18 18"><path d="M4 2l3 3-1.5 2a9 9 0 0 0 5.5 5.5L13 11l3 3-2 2C8 16 2 10 2 4z" fill="#111"/></svg>
        <span>+61 417 532 148</span>
      </li>
      <li class="contacts__item">
        <svg class="contacts__icon" viewBox="0 0 18 18"><rect x="1" y="4" width="16" height="11" fill="#111"/><path d="M1 4l8 6 8-6" stroke="#e4542a" stroke-width="1.2" fill="none"/></svg>
        <span>carl@brimstead.example.au</span>
      </li>
    </ul>
  </section>

</body>
</html>
```